fry fang: flyer/menu board design for modern food van/trailer concept.

who are we? a modern food van/trailer selling restuarant quality food (burrito, burgers, waffles).our demographic is 16 - 35.

what do we need? a design for a flyer A4 size that is divided in 3 sections.with our menu on the inside and a design on the outside with our logo. the style must be funky, cool and modern.

Our restaurant theme is based on the movie "dusk blade" by marcus halloway. So any designs should be somehow linked to that genre.

the same menu on the flyer will be posted on our menu board. there is a chance we will use an lcd menu board so the format must accomodate that.
the menu must also be easilly modified in case we need to update changes pricing and menu items.

thank you
team fry fang

Hi, Project will become non-refundable as soon as i get some good designs. Thank you and good luck Team fry fang

Dear designers, I have uploaded some example menus, pics, my logo and hand drawings of my vision of how i would like the flyer/menu to look like. I understand that some designers cant see my uploads. I have contacted pixel forge and they are trying to fix the issue. The deadline will be extended if needed. Thank you for your patients and your designs. Regards, Rory

Hi, To those who are having trouble viewing my uploads, here is the link http://jobs.pixelforgehub.com/job.aspx?id=318560

Target Market(s)

our target market is young and cool between the ages of16 - 35. we are a multicultural society in a western governed country. Sydney Australia.

Industry/Entity Type

Restaurant

Font styles to use
Serif

Requirements
Must have
• pictures of menu items in a hand drawn black and white style: burger, burrito, waffles, buffallo wings, chicken, beef, prawn. examples provided
please feel free to show off your alternate ideas.
style should be modern, cool and funky. examples provided
Nice to have
• Colours: yellow, red, black.
Pictures/illustrations: black & white in a sketch style.
Theme: ninja, Mexican, modern, funky.

```html
<!DOCTYPE html>
<html lang="en">
<head>
<meta charset="utf-8">
<title>Fry Fang – Menu</title>
<link rel="stylesheet" href="https://fonts.googleapis.com/css2?family=Alfa+Slab+One&family=Roboto+Slab:wght@700&family=Indie+Flower&display=swap">
<style>
:root{
  --bg-core:#7a1526;
  --bg-edge:#2a0508;
  --red:#e0141b;
  --red-deep:#a80d12;
  --yellow:#ffe23a;
  --gold:#f3c93c;
  --orange:#f07b1c;
  --tan:#c9a27a;
  --green:#8dbb3a;
  --blue:#6fb7c4;
  --violet:#b07ad6;
  --rose:#e26a8a;
  --pink:#ff7fd0;
  --chalk:#e9e0d6;
  --white:#ffffff;
  --ink:#111111;
  --sketch:#d9d2cc;
}
*{margin:0;padding:0;box-sizing:border-box}
html,body{width:1200px;height:848px;overflow:hidden;background:var(--bg-edge)}
.menu{position:relative;width:1200px;height:848px;overflow:hidden;
  background:radial-gradient(ellipse at 50% 40%,var(--bg-core) 0%,#4f0c15 55%,var(--bg-edge) 100%);
  font-family:"Roboto Slab",serif;color:var(--white)}
.abs{position:absolute;white-space:nowrap}
.sketch{position:absolute;background:radial-gradient(circle,#f4f1ee 0%,var(--sketch) 70%);border-radius:10px;opacity:.9}
.title{font-family:"Alfa Slab One",serif;letter-spacing:1px;font-weight:400}
.slab{font-family:"Alfa Slab One",serif;letter-spacing:1px}
.hand{font-family:"Indie Flower",cursive;font-weight:700}
.item-name{font-family:"Alfa Slab One",serif;font-size:19px;line-height:20px;letter-spacing:1px;text-align:center}
.item-desc{font-size:12px;line-height:15px;text-align:center;color:var(--white)}
.price-tag{position:absolute;width:80px;height:34px;background:var(--white);color:var(--ink);
  clip-path:polygon(0 10%,100% 0,88% 50%,100% 100%,0 90%,10% 50%);
  font-family:"Alfa Slab One",serif;font-size:22px;display:flex;align-items:center;justify-content:center}
.step{position:absolute;left:10px;width:300px;height:60px}
.step svg{position:absolute;inset:0}
.step .lead{position:absolute;top:5px;width:100%;text-align:center;font-family:"Alfa Slab One",serif;font-size:14px;line-height:16px;white-space:nowrap}
.step .num{position:absolute;top:27px;width:100%;text-align:center;font-family:"Alfa Slab One",serif;font-size:22px;line-height:26px}
.left{position:absolute;left:10px;width:300px}
.mid{position:absolute;left:390px;width:420px}
.extras{font-family:"Alfa Slab One",serif;color:var(--gold);font-size:20px;line-height:26px}
</style>
</head>
<body>
<main class="menu">

  <header class="abs" style="left:120px;top:30px;display:flex;align-items:center;gap:8px">
    <span style="display:inline-block;width:18px;height:18px;border-radius:50%;background:var(--yellow)"></span>
    <span class="title" style="font-size:28px;color:var(--yellow)">Fry Fang</span>
  </header>

  <section aria-label="Burrito">
    <h2 class="title abs" style="left:38px;top:132px;font-size:28px;color:var(--red);background:var(--white);padding:2px 10px;transform:rotate(-6deg);border-radius:4px">BURRITO</h2>
    <div class="price-tag" style="left:75px;top:170px">$9</div>
    <div class="sketch" role="img" aria-label="Sketch of a wrapped burrito" style="left:272px;top:96px;width:70px;height:48px"></div>
    <p class="title abs" style="left:238px;top:152px;font-size:12px;line-height:15px;color:var(--red);background:var(--white);padding:2px 6px;transform:rotate(-3deg)">WHATS A BURRITO?!<br>A MEXICAN KEBAB <span style="font-size:20px">MATE!</span></p>

    <div class="step" style="top:220px">
      <svg width="300" height="60" viewBox="0 0 300 60"><path d="M0 20 L25 10 L35 30 L0 45 Z M300 20 L275 10 L265 30 L300 45 Z" fill="var(--red-deep)"/><rect x="25" y="2" width="250" height="22" fill="var(--red)"/><rect x="20" y="26" width="260" height="28" fill="var(--red)"/></svg>
      <div class="lead" style="color:var(--yellow)">CHOOSE YOUR STYLE</div>
      <div class="num" style="color:var(--yellow)">STEP#1</div>
    </div>
    <div class="left" style="top:280px">
      <div class="item-name" style="color:var(--tan)">ORIGINAL</div>
      <div class="item-desc">Lettuce, salsa, guacamole &amp; sour cream.</div>
      <div class="item-name" style="color:var(--green);margin-top:3px">FAJITA</div>
      <div class="item-desc">Grilled capsicum &amp; onion, salsa, guacamole &amp; sour cream.</div>
      <div class="item-name" style="color:var(--blue);margin-top:3px">CALIFORNIA</div>
      <div class="item-desc">Fries, cheese, salsa, guacamole &amp; sour cream.</div>
    </div>

    <div class="step" style="top:395px">
      <svg width="300" height="60" viewBox="0 0 300 60"><path d="M0 5 L40 15 L30 40 L0 30 Z M300 5 L260 15 L270 40 L300 30 Z" fill="#d9a400"/><rect x="25" y="3" width="250" height="22" fill="var(--yellow)"/><rect x="30" y="27" width="240" height="28" fill="var(--yellow)"/></svg>
      <div class="lead" style="color:var(--red)">CHOOSE YOUR FILLING</div>
      <div class="num" style="color:var(--red)">STEP#2</div>
    </div>
    <div class="left" style="top:456px">
      <div class="item-name" style="color:var(--tan)">MEXICAN CHICKEN:</div>
      <div class="item-desc">marinated breast fillet.</div>
      <div class="item-name" style="color:var(--green);margin-top:2px">CHIPOTLE STEAK:</div>
      <div class="item-desc">juicy char grilled steak</div>
      <div class="item-name" style="color:var(--tan);margin-top:2px">FISH FILLET:</div>
      <div class="item-desc">flash fried.</div>
      <div class="item-name" style="color:var(--orange);margin-top:2px">SAUTE PRAWN:</div>
      <div class="item-desc">with lemon &amp; herb</div>
    </div>
    <div class="sketch" role="img" aria-label="Sketch of a fish" style="left:295px;top:527px;width:48px;height:24px"></div>
    <div class="sketch" role="img" aria-label="Sketch of a prawn" style="left:280px;top:563px;width:34px;height:28px"></div>

    <div class="step" style="top:605px">
      <svg width="300" height="60" viewBox="0 0 300 60"><path d="M0 20 L25 10 L35 30 L0 45 Z M300 20 L275 10 L265 30 L300 45 Z" fill="var(--red-deep)"/><rect x="25" y="2" width="250" height="22" fill="var(--red)"/><rect x="20" y="26" width="260" height="28" fill="var(--red)"/></svg>
      <div class="lead" style="color:var(--yellow)">ADD A SAUCE (OPTIONAL)</div>
      <div class="num" style="color:var(--yellow)">STEP#3</div>
    </div>
    <ul class="abs slab" style="left:14px;top:668px;list-style:none;font-size:15px;line-height:17px">
      <li style="color:var(--green)">CORRIANDER &amp; LIME (MILD)</li>
      <li style="color:var(--chalk)">CHIPOTLE (MEDIUM)</li>
      <li style="color:var(--gold)">HOT SAUCE (HOT)</li>
      <li style="color:var(--red)">HABANNERO (INSANE)</li>
    </ul>
    <div class="sketch" role="img" aria-label="Sketch of a chilli" style="left:262px;top:680px;width:30px;height:38px"></div>
    <div class="abs extras" style="left:88px;top:758px">EXTRAS: $1<br>GUACAMOLE $2<br>EXTRA FILLING $3</div>
  </section>

  <section aria-label="Burgers">
    <div class="sketch" role="img" aria-label="Sketch of a burger" style="left:500px;top:15px;width:110px;height:70px"></div>
    <div class="price-tag" style="left:640px;top:45px;width:70px">$9</div>
    <svg class="abs" style="left:475px;top:78px" width="210" height="40" viewBox="0 0 210 40"><path d="M0 8 L20 12 L12 22 L0 34 Z M210 8 L190 12 L198 22 L210 34 Z" fill="#a8480f"/><rect x="15" y="4" width="180" height="30" fill="var(--orange)"/></svg>
    <h2 class="title abs" style="left:475px;top:84px;width:210px;text-align:center;font-size:20px;line-height:24px">BURGERS</h2>
    <p class="abs slab" style="left:530px;top:116px;width:100px;text-align:center;font-size:10px;line-height:11px">OUT OF THIS<br>WORLD!</p>
    <p class="abs slab" style="left:520px;top:138px;font-size:24px;line-height:28px;color:var(--orange)">200g BEEF</p>
    <p class="abs hand" style="left:500px;top:166px;font-size:20px;color:var(--yellow)">You got beef wid dat?</p>
    <div class="sketch" role="img" aria-label="Sketch of a steak" style="left:700px;top:172px;width:60px;height:34px"></div>
    <div class="mid" style="top:206px">
      <div class="item-name" style="color:var(--gold)">CLASSIC BEEF</div>
      <div class="item-desc">Lettuce, tomato, grilled onion, bbq sauce.</div>
      <div class="item-name" style="color:var(--green)">AUSSIE BURGER</div>
      <div class="item-desc">Lettuce, tomato, grilled onion, pineapple, beef rashes, bbq sauce.</div>
      <div class="item-name" style="color:var(--blue)">AMERICAN</div>
      <div class="item-desc">Coleslaw, tomatoe, fries, pickles, mayo, ketchup.</div>
      <div class="item-name" style="color:var(--orange)">CHEESE BURGER</div>
      <div class="item-desc">Cheese, pickles, onion, mustard, ketchup, mayo</div>
      <div class="item-name" style="color:var(--violet)">BACKYARD BURGER</div>
      <div class="item-desc">Lettuce, tomato, cheese, pickles, onion, mustard, ketchup, mayo.</div>
      <div class="item-name" style="color:var(--gold)">SURF N TURF</div>
      <div class="item-desc">Lettuce, tomatoe, calamari, harrissa paste, ketchup, mayo.</div>
    </div>
  </section>

  <section aria-label="Chicken">
    <h2 class="title abs" style="left:520px;top:424px;font-size:24px;line-height:28px;color:var(--yellow)">CHICKEN</h2>
    <p class="abs hand" style="left:575px;top:450px;font-size:13px;color:var(--yellow)">Mmm chikken...</p>
    <div class="sketch" role="img" aria-label="Sketch of a roast chicken" style="left:418px;top:452px;width:80px;height:56px"></div>
    <div class="mid" style="top:476px">
      <div class="item-name" style="color:var(--tan)">CLASSIC CHICKEN</div>
      <div class="item-desc">Lettuce, mayo.</div>
      <div class="item-name" style="color:var(--gold)">KRISPY</div>
      <div class="item-desc">Crispy chicken tenders, lettuce, cheese, feisty mayo.</div>
      <div class="item-name" style="color:var(--green)">CHICKEN N CHIPS</div>
      <div class="item-desc">Crispy chicken tenders, fries, coleslaw, cheese, feisty mayo.</div>
      <div class="item-name" style="color:var(--red)">MEXICAN</div>
      <div class="item-desc">Grilled chicken breast, lettuce, salsa, guacamole, southwest sauce.</div>
      <div class="item-name" style="color:var(--rose)">PORTUGUESE</div>
      <div class="item-desc">Grilled chicken breast, lettuce, cheese, mayo, perri perri.</div>
      <div class="item-name" style="color:var(--green)">LEBANESE</div>
      <div class="item-desc">Grilled chicken breast, fries, Lebanese pickles, garlic sauce.</div>
    </div>
    <div class="abs extras" style="left:550px;top:718px">EXTRAS: $1<br>GUACAMOLE $2<br>DOUBLE BEEF<br>OR CHICKEN</div>
    <p class="abs slab" style="left:718px;top:764px;font-size:20px;line-height:26px;color:var(--gold)">$4.50</p>
    <p class="abs" style="left:550px;top:824px;font-size:11px;color:var(--gold)">(MAKE SURE YOUR HUNGRY)</p>
  </section>

  <section aria-label="Meal deal" class="abs" style="left:322px;top:690px;width:190px;height:158px;background:#5a1a12">
    <div class="sketch" role="img" aria-label="Sketch of fries, a drink and sauce bottle" style="left:8px;top:4px;width:90px;height:60px"></div>
    <p class="abs title" style="left:104px;top:8px;font-size:28px;line-height:30px;color:var(--red);text-align:center;transform:rotate(-8deg)">4.50<br>$</p>
    <p class="abs slab" style="left:6px;top:80px;font-size:13px;color:var(--ink);transform:rotate(-10deg)">MAKE IT A</p>
    <p class="abs title" style="left:14px;top:86px;font-size:36px;line-height:40px;color:var(--red);transform:rotate(-10deg)">MEAL</p>
    <p class="abs slab" style="left:70px;top:124px;font-size:11px;line-height:13px;text-align:center;transform:rotate(-10deg)">FRIES, SAUCE &amp;<br>DRINK</p>
  </section>

  <section aria-label="Buffalo chicken ribs">
    <div class="sketch" role="img" aria-label="Sketch of chicken wings" style="left:805px;top:15px;width:125px;height:55px"></div>
    <h2 class="title abs" style="left:822px;top:66px;width:122px;text-align:center;font-size:20px;line-height:26px;color:var(--orange);white-space:normal">BUFFALO CHICKEN RIBS</h2>
    <p class="abs hand" style="left:952px;top:56px;width:245px;font-size:22px;line-height:30px;color:var(--yellow);white-space:normal">Is when a buffalo makes love to a chicken... drenched in sauce &amp; Served with ranch.</p>
    <p class="abs hand" style="left:840px;top:176px;font-size:22px;color:var(--yellow)">-sauces-</p>
    <p class="abs slab" style="left:808px;top:207px;font-size:11px;letter-spacing:.5px">- LEMON &amp; HERBS, BBQ, HOT SAUCE, PERRI PERRI -</p>
    <div class="abs slab" style="left:845px;top:228px;font-size:28px;line-height:36px;color:var(--chalk)">
      <div>6 x <span class="sketch" role="img" aria-label="Wing icon" style="position:relative;display:inline-block;width:36px;height:14px"></span> = $4.95</div>
      <div style="color:var(--tan)">12 x <span class="sketch" role="img" aria-label="Wing icon" style="position:relative;display:inline-block;width:36px;height:14px"></span> = $7.95</div>
      <div style="color:var(--green)">24 x <span class="sketch" role="img" aria-label="Wing icon" style="position:relative;display:inline-block;width:36px;height:14px"></span> = $14.95</div>
    </div>
  </section>

  <section aria-label="Nachos">
    <div class="sketch" role="img" aria-label="Sketch of a bowl of nachos" style="left:815px;top:345px;width:115px;height:60px"></div>
    <h2 class="title abs" style="left:808px;top:404px;font-size:32px;line-height:38px;color:var(--yellow)">NACHOS</h2>
    <div class="abs" style="left:975px;top:355px;width:190px;white-space:normal">
      <div class="item-name" style="color:var(--blue)">NACHOS<br>GUACAMOLE</div>
      <div class="item-desc" style="font-size:13px">Corn chips, salsa, guacamole, sour cream &amp; cheese.</div>
    </div>
    <div class="price-tag" style="left:1050px;top:436px">$7</div>
    <div class="abs" style="left:820px;top:455px;width:170px;white-space:normal">
      <div class="item-name" style="color:var(--orange)">NACHOS<br>BEEF</div>
      <div class="item-desc" style="font-size:13px">Corn chips salsa, beef chilli, sour cream &amp; cheese.</div>
    </div>
    <div class="price-tag" style="left:872px;top:527px">$7</div>
    <div class="abs" style="left:1010px;top:482px;width:130px;white-space:normal">
      <div class="item-name" style="color:var(--green)">MACHO<br>NACHOS</div>
      <div class="item-desc" style="font-size:13px">All of the above</div>
    </div>
    <div class="price-tag" style="left:1030px;top:548px">$9</div>
  </section>

  <section aria-label="Fries">
    <div class="sketch" role="img" aria-label="Sketch of a fries carton" style="left:815px;top:575px;width:58px;height:75px"></div>
    <div class="price-tag" style="left:868px;top:605px;width:70px">$4</div>
    <h2 class="title abs" style="left:915px;top:588px;font-size:26px;line-height:30px;color:var(--yellow)">FRIES</h2>
  </section>

  <section aria-label="Belgian waffles">
    <p class="abs hand" style="left:1085px;top:612px;font-size:15px;color:var(--red);transform:rotate(-4deg)">NOT FROZEN</p>
    <div class="sketch" role="img" aria-label="Sketch of Belgian waffles" style="left:1030px;top:630px;width:140px;height:50px"></div>
    <div class="price-tag" style="left:975px;top:645px;width:75px">$10</div>
    <h2 class="title abs" style="left:910px;top:680px;font-size:22px;line-height:26px;color:var(--pink)">BELGIAN WAFFLES</h2>
    <p class="abs hand" style="left:805px;top:706px;width:392px;font-size:17px;line-height:20px;color:var(--yellow);white-space:normal">House made waffles freshly made while you wait! Served with fresh strawberries, pure Canadian maple syrup, Belgian chocolate and fresh cream. Enough said.</p>
    <p class="abs" style="left:800px;top:802px;width:396px;height:44px;background:var(--yellow);color:var(--ink);font-size:8.5px;line-height:11px;padding:3px 6px;text-align:center;white-space:normal">WE SOURCE AND USE THE BEST QUALITY INGREDIENTS AND SERVE IT THE FRESHEST WAY POSSIBLE. ALL MENU ITEMS HAVE BEEN PREPARED WITH CARE AND ARE COOKED FRESH WHILE YOU WAIT. PLEASE BEPATIENT AS YOUR FOOD IS BEING MADE.</p>
  </section>

</main>
</body>
</html>
```